Car Design - New van

It's Marisol and Tom from Larkin the Plumber.

Below is the vehicle - it is a Rovanta Kesslo. I have another company with the type of look we are chasing with your creative flair thrown in.

* We would like the Larkin the Plumber Logo to be as large as possible
on the side of the van along with the phone numbers

* The back of the van we would like the logo to be as large as possible with the phone numbers.

* We would like the Larkin the plumber web address www.larkintheplumber.com.au to be placed along bottom of vehicle as per the previous trucks. And of course phone numbers to be as large as possible without over bearing.

thanks
Marisol

```html
<!DOCTYPE html>
<html lang="en">
<head>
<meta charset="utf-8">
<title>Larkin the Plumber – Van Wrap</title>
<link href="https://fonts.googleapis.com/css2?family=Barlow+Condensed:ital,wght@0,600;0,700;1,700&family=Roboto:wght@500;900&display=swap" rel="stylesheet">
<style>
  :root {
    --wrap-blue: #2b3a97;
    --wrap-red: #e8202e;
    --white: #ffffff;
    --ink: #111111;
    --glass: #d9dade;
    --page: #ffffff;
  }
  html, body {
    margin: 0;
    width: 1200px;
    height: 985px;
    overflow: hidden;
    background: var(--page);
  }
  .wrap-sheet { display: block; width: 1200px; height: 985px; }
  .panel-blue { fill: var(--wrap-blue); }
  .panel-red { fill: var(--wrap-red); }
  .window { fill: var(--glass); }
  .wheel-arch { fill: var(--page); }
  .logo-disc { fill: var(--white); stroke: var(--ink); stroke-width: 6; }
  .logo-ring { fill: none; stroke: var(--ink); stroke-width: 3; }
  .logo-name {
    font-family: 'Barlow Condensed', sans-serif;
    font-weight: 700;
    fill: var(--ink);
    text-anchor: middle;
    letter-spacing: 2px;
  }
  .logo-est {
    font-family: 'Roboto', sans-serif;
    font-weight: 500;
    font-size: 28px;
    fill: var(--ink);
    text-anchor: middle;
  }
  .tagline {
    font-family: 'Barlow Condensed', sans-serif;
    font-weight: 700;
    font-size: 46px;
    fill: var(--white);
    text-anchor: middle;
  }
  .credentials {
    font-family: 'Barlow Condensed', sans-serif;
    font-weight: 600;
    font-size: 21px;
    fill: var(--white);
    text-anchor: middle;
  }
  .phone {
    font-family: 'Barlow Condensed', sans-serif;
    font-style: italic;
    font-weight: 700;
    font-size: 58px;
    fill: var(--white);
    text-anchor: middle;
    letter-spacing: 1px;
  }
  .web {
    font-family: 'Barlow Condensed', sans-serif;
    font-style: italic;
    font-weight: 700;
    font-size: 26px;
    fill: var(--white);
    text-anchor: middle;
  }
  .social-dot { fill: none; stroke: var(--white); stroke-width: 2.5; }
  .social-name {
    font-family: 'Barlow Condensed', sans-serif;
    font-weight: 600;
    font-size: 15px;
    fill: var(--white);
  }
</style>
</head>
<body>
<svg class="wrap-sheet" viewBox="0 0 1500 1231" xmlns="http://www.w3.org/2000/svg" aria-label="Larkin the Plumber van wrap, both sides">
  <defs>
    <path id="van-body" d="M70 500 L70 300 Q75 110 120 75 Q140 55 200 52 L700 50 Q950 55 1040 110 L1180 230 Q1320 280 1400 320 Q1440 340 1440 420 L1440 500 Q1440 520 1420 520 L90 520 Q70 520 70 500 Z"/>
    <clipPath id="van-clip"><use href="#van-body"/></clipPath>
    <g id="van-wrap">
      <use href="#van-body" class="panel-red"/>
      <path class="panel-blue" clip-path="url(#van-clip)" d="M0 0 L610 0 L430 560 L0 560 Z"/>
      <path class="window" d="M770 130 L985 128 Q1060 150 1135 250 L775 275 Z"/>
      <circle class="wheel-arch" cx="330" cy="530" r="100"/>
      <circle class="wheel-arch" cx="1210" cy="530" r="100"/>
      <circle class="logo-disc" cx="580" cy="285" r="225"/>
      <circle class="logo-ring" cx="580" cy="285" r="165"/>
    </g>
  </defs>

  <!-- Driver side -->
  <g class="van van-driver-side">
    <use href="#van-wrap"/>
    <g class="brand-logo">
      <text class="logo-name" x="580" y="265" font-size="62">LARKIN</text>
      <text class="logo-name" x="580" y="320" font-size="40">THE PLUMBER</text>
      <text class="logo-est" x="580" y="418">Est. 1978</text>
    </g>
    <text class="tagline" x="245" y="148">Dedicated</text>
    <text class="tagline" x="245" y="196">Plumbing</text>
    <text class="tagline" x="245" y="245">Specialists</text>
    <g class="social-links">
      <circle class="social-dot" cx="152" cy="322" r="9"/><text class="social-name" x="165" y="327">Nook</text>
      <circle class="social-dot" cx="202" cy="322" r="9"/><text class="social-name" x="215" y="327">Chirp</text>
      <circle class="social-dot" cx="152" cy="374" r="9"/><text class="social-name" x="165" y="379">Snapr</text>
      <circle class="social-dot" cx="202" cy="374" r="9"/><text class="social-name" x="215" y="379">Loop</text>
    </g>
    <text class="credentials" x="944" y="358">Trusted Plumbers Since 1978</text>
    <text class="credentials" x="944" y="381">Over 40 Years Of Experience</text>
    <text class="phone" x="928" y="470">07 5550 1928</text>
    <text class="web" x="936" y="499">larkintheplumber.com.au</text>
  </g>

  <!-- Passenger side -->
  <g class="van van-passenger-side">
    <use href="#van-wrap" transform="translate(1500 615) scale(-1 1)"/>
    <g class="brand-logo">
      <text class="logo-name" x="920" y="880" font-size="62">LARKIN</text>
      <text class="logo-name" x="920" y="935" font-size="40">THE PLUMBER</text>
      <text class="logo-est" x="920" y="1033">Est. 1978</text>
    </g>
    <text class="tagline" x="1255" y="763">Dedicated</text>
    <text class="tagline" x="1255" y="811">Plumbing</text>
    <text class="tagline" x="1255" y="860">Specialists</text>
    <g class="social-links">
      <circle class="social-dot" cx="1272" cy="938" r="9"/><text class="social-name" x="1285" y="943">Nook</text>
      <circle class="social-dot" cx="1322" cy="938" r="9"/><text class="social-name" x="1335" y="943">Chirp</text>
      <circle class="social-dot" cx="1272" cy="990" r="9"/><text class="social-name" x="1285" y="995">Snapr</text>
      <circle class="social-dot" cx="1322" cy="990" r="9"/><text class="social-name" x="1335" y="995">Loop</text>
    </g>
    <text class="credentials" x="536" y="975">Trusted Plumbers Since 1978</text>
    <text class="credentials" x="536" y="998">Over 40 Years Of Experience</text>
    <text class="phone" x="568" y="1085">07 5550 1928</text>
    <text class="web" x="568" y="1114">larkintheplumber.com.au</text>
  </g>
</svg>
</body>
</html>
```